Trindle Salve by Petal Wrens: All Natural Lip Balm Co. Looking for New Label

Greetings, our company is called Petal Wrens and we are a start-up founded in early 2014. We make 100% All-Natural lip balm, called Trindle Salve, in a variety of flavors and we are looking for a new label that incorporates part of our logo and highlights our product name and our lip balms flavor (see attached files). Our website is: trindlesalve.example, and we are on Twitter: @PetalWrensSalves, and Facebook: /PetalWrensSalves. Our lip balms are made with beeswax, sweet almond oil, shea butter, coconut oil and other all natural oils and flavors.

The design should be clean, and communicate comfort, its "all-natural-ness", reliability, and fun. The colors we would like to have incorporated are burgundy, a deep, but not dark orange (see files, website, logo, graphics), some green and maybe gold/yellow. Given that the lip balm tubes are small (standard tubes), we would like to assure that the lip balm name, the flavor, and part of the logo- (perhaps the bee), are clearly visible and easily read. I am open to a variety of fonts, as long as they convey what I have stated above.

We want to use the label graphics and our logo for not only labeling our product, but also for use on our website, on banners, signs, retail boxes, letterhead, tee shirts, etc. If we like the design we are open to working with you again as our company is growing and we will be expanding our product line within the year to include hand and body balms, as well as other similar items and we will eventually have a few different product lines marketed at various age groups as well. Our lip balm is currently marketed to 14 to 40+ demographic, with the average age being roughly in the 15 to 24 range and our lip balm has been purchased by more women than men, though we market to both.

As far as software goes, I would like it to be in a format that is most popular- my old logo and graphics were made in Adobe Creative Suite 5.0, Adobe InDesign, and Adobe Illustrator, so the label should be made using this software (or a higher version). If I can have the label in a JPEG format also so I personally can add it to my website and social media that would be great.

I have a label redesign doc in an indd format but it was too large to upload. I believe this was the entire layout of our last label. If you need this, or anything else, please let me know as well as how I can send it to you.

We have applied to the popular TV show Otter Court and recently received a call back with interest from the producers; we are so excited and hope you are as well!

Thank you!
Gregor Tallowby
Owner
Petal Wrens Salves LLC
Gregor@PetalWrensSalves.example

The Label dimensions are: 2.25 inches wide ---> by 2 inches long. Currently, there is a .75 inch area that is part of the label and is perforated, used as a safety seal. I may be changing the labels to a slightly different kind but the dimensions will be the same. The tubes we use are standard lip balm tubes with a net weight of .15 ounces ( the total length of the tube from the bottom turning piece to the top of the cap is just over 2.5 inches (this is NOT how large the label must be).We are discontinuing the 1 Hive, 2 Hive concepts ( for different consistencies of the balm) so that part of the label does not need to be included.Feel free to enhance and/or modify the logo to fit the design of the label.Thank you! Added Thursday, February 12, 2015

Requirements
Must have
• Label Dimensions:
• Length: 2.125" Height: 2.125"
• Top Margin: 1.025" Bottom Margin: 1.025"
• Left Margin: 0.9125" Right Margin: 0.9125"
• Horizontal Spacing: 0.15" Vertical Spacing: 0.15"
• Horizontal Pitch: 2.275" Vertical Pitch: 2.275"

```html
<!DOCTYPE html>
<html lang="en">
<head>
<meta charset="utf-8">
<title>Trindle Salve – Citrus Cloudpuff Label</title>
<link rel="stylesheet" href="https://fonts.googleapis.com/css2?family=Poiret+One&family=Arimo:wght@400&display=swap">
<style>
  :root {
    --canvas: #ffffff;
    --frame-orange: #f7a21b;
    --rule-orange: #f26522;
    --name-green: #5ccf1c;
    --flavor-orange: #f7941d;
    --ink-grey: #4a4a4a;
    --panel-orange: #ff6a00;
    --panel-glow: #fde3cc;
    --white: #ffffff;
    --bee-black: #1f1f1f;
    --bee-amber: #f9a11b;
    --bee-green: #6dd34a;
  }
  * { box-sizing: border-box; margin: 0; padding: 0; }
  html, body {
    width: 1200px;
    height: 581px;
    overflow: hidden;
    background: var(--canvas);
  }
  .canvas {
    position: relative;
    width: 1200px;
    height: 581px;
    font-family: "Poiret One", "Century Gothic", sans-serif;
    font-weight: 400;
  }
  .label {
    position: absolute;
    overflow: hidden;
  }
  .label--light {
    left: 0;
    top: 0;
    width: 518px;
    height: 581px;
    background: var(--white);
    border: 9px solid var(--frame-orange);
    border-radius: 10px;
  }
  .label--bold {
    left: 696px;
    top: 10px;
    width: 504px;
    height: 565px;
    background: radial-gradient(circle at 50% 58%, var(--panel-glow) 0%, #fcc497 22%, #ff9a45 48%, var(--panel-orange) 78%);
  }

  .seal-rule {
    position: absolute;
    left: 0;
    right: 0;
    height: 3px;
  }
  .label--light .seal-rule {
    top: 186px;
    background: repeating-linear-gradient(90deg, var(--rule-orange) 0 20px, transparent 20px 34px);
  }
  .label--bold .seal-rule {
    top: 189px;
    background: repeating-linear-gradient(90deg, var(--white) 0 20px, transparent 20px 34px);
  }

  .brand-tag {
    position: absolute;
    width: 278px;
    height: 78px;
    border: 3px solid;
    padding: 6px 0 0 18px;
  }
  .label--light .brand-tag { left: 111px; top: 46px; border-color: var(--flavor-orange); }
  .label--bold .brand-tag { left: 114px; top: 50px; border-color: var(--white); width: 276px; }
  .brand-tag__name {
    font-size: 32px;
    line-height: 34px;
    white-space: nowrap;
  }
  .brand-tag__flavor {
    font-size: 17px;
    line-height: 18px;
    margin-left: 18px;
    white-space: nowrap;
  }
  .brand-tag__dot {
    position: absolute;
    right: 12px;
    top: 14px;
    width: 30px;
    height: 30px;
    border-radius: 50%;
  }
  .label--light .brand-tag__name { color: var(--name-green); }
  .label--light .brand-tag__flavor { color: var(--flavor-orange); }
  .label--light .brand-tag__dot { background: var(--bee-amber); }
  .label--bold .brand-tag__name,
  .label--bold .brand-tag__flavor { color: var(--white); }
  .label--bold .brand-tag__dot { background: var(--white); }

  .mascot {
    position: absolute;
    width: 275px;
    height: 215px;
    border-radius: 45% 50% 40% 45%;
    opacity: 0.85;
  }
  .label--light .mascot {
    left: 91px;
    top: 226px;
    background: linear-gradient(135deg, var(--bee-green) 0%, #c9efb6 25%, var(--bee-amber) 50%, var(--bee-black) 70%, var(--bee-amber) 85%);
  }
  .label--bold .mascot {
    left: 94px;
    top: 222px;
    background: linear-gradient(135deg, var(--bee-green) 0%, #d7f3c8 25%, var(--bee-amber) 50%, var(--bee-black) 70%, var(--bee-amber) 85%);
  }

  .product {
    position: absolute;
    left: 0;
    right: 0;
    text-align: center;
  }
  .label--light .product { top: 448px; }
  .label--bold .product { top: 444px; }
  .product__name {
    font-size: 50px;
    font-weight: 400;
    line-height: 56px;
    letter-spacing: 0.5px;
    white-space: nowrap;
  }
  .product__flavor {
    font-size: 25px;
    line-height: 26px;
    white-space: nowrap;
  }
  .product__kind {
    font-family: "Arimo", Arial, sans-serif;
    font-size: 13px;
    line-height: 15px;
  }
  .label--light .product__name { color: var(--name-green); }
  .label--light .product__flavor { color: var(--flavor-orange); }
  .label--light .product__kind { color: var(--ink-grey); }
  .label--bold .product__name,
  .label--bold .product__flavor,
  .label--bold .product__kind { color: var(--white); }
</style>
</head>
<body>
<main class="canvas">

  <section class="label label--light" aria-label="Label on white">
    <div class="brand-tag">
      <p class="brand-tag__name">Trindle Salve</p>
      <p class="brand-tag__flavor">Citrus Cloudpuff</p>
      <span class="brand-tag__dot" aria-hidden="true"></span>
    </div>
    <div class="seal-rule" aria-hidden="true"></div>
    <div class="mascot" role="img" aria-label="Cartoon honeybee with green wings and orange and black stripes, flying to the right"></div>
    <div class="product">
      <h1 class="product__name">Trindle Salve</h1>
      <p class="product__flavor">Citrus Cloudpuff</p>
      <p class="product__kind">beewax lip balm</p>
    </div>
  </section>

  <section class="label label--bold" aria-label="Label on orange">
    <div class="brand-tag">
      <p class="brand-tag__name">Trindle Salve</p>
      <p class="brand-tag__flavor">Citrus Cloudpuff</p>
      <span class="brand-tag__dot" aria-hidden="true"></span>
    </div>
    <div class="seal-rule" aria-hidden="true"></div>
    <div class="mascot" role="img" aria-label="Cartoon honeybee with green wings and orange and black stripes, flying to the right"></div>
    <div class="product">
      <h2 class="product__name">Trindle Salve</h2>
      <p class="product__flavor">Citrus Cloudpuff</p>
      <p class="product__kind">beewax lip balm</p>
    </div>
  </section>

</main>
</body>
</html>
```